Courier Business - Wordpress Design Project

Looking for a designer that can develop a 5 page clean website for a company I have a steak in,

http://parcel-brisk.example.com.au/

is the current website and I looks terrible,

The logo is hosted on the current site

Target Market(s)

Business to Business

Industry/Entity Type

Business

Requirements
Must have
• Clean, aesthetic and use free stock images

A google map with the office location

```html
<!DOCTYPE html>
<html lang="en">
<head>
<meta charset="utf-8">
<title>Parcel Brisk Couriers</title>
<link href="https://fonts.googleapis.com/css2?family=PT+Sans:wght@400;700&family=Arimo:wght@400;700&display=swap" rel="stylesheet">
<style>
:root{
  --orange:#f05a28;
  --navy:#1b4a6e;
  --navy-dark:#163d5c;
  --ink:#222;
  --grey-text:#555;
  --light:#f4f4f4;
  --line:#c9c9c9;
  --blue:#1e88d6;
  --footer:#3a3a3a;
}
*{box-sizing:border-box;margin:0;padding:0}
html,body{width:814px;height:1200px;overflow:hidden}
body{position:relative;background:#fff;font-family:"Arimo",Arial,sans-serif;color:var(--ink)}
.abs{position:absolute}
.header{left:0;top:0;width:814px;height:98px;background:linear-gradient(#fff,#f1f1f1)}
.brand{display:flex;align-items:center;gap:6px;font-family:"PT Sans",sans-serif;font-size:19px;color:var(--navy-dark)}
.brand .dot{width:14px;height:14px;border-radius:50%;background:var(--orange)}
.header .brand{left:80px;top:40px}
.account{right:82px;top:9px;font-family:"PT Sans",sans-serif;font-size:10px;color:#222}
.follow-label{left:676px;top:58px;font-family:"PT Sans",sans-serif;font-size:10px}
.social-icons{left:626px;top:73px;display:flex;gap:4px}
.social-icons span{width:15px;height:15px;border-radius:3px;display:block}
.nav{left:0;top:98px;width:814px;height:32px;background:var(--navy);display:flex;align-items:center}
.nav a{position:absolute;color:#fff;font-family:"PT Sans",sans-serif;font-size:10px;text-decoration:none;transform:translateX(-50%)}
.nav .home{left:79px;top:4px;width:57px;height:23px;background:#2a2a2a;border:1px solid #555;border-radius:2px;transform:none;text-align:center;line-height:21px}
.nav .sep{position:absolute;top:6px;width:1px;height:20px;background:#2f5e82}
.band{left:0;top:298px;width:814px;height:312px;background:var(--orange)}
.hero-frame{left:69px;top:146px;width:677px;height:287px;background:#fff;box-shadow:0 6px 14px rgba(0,0,0,.25)}
.hero-img{left:70px;top:152px;width:675px;height:276px;background:linear-gradient(100deg,#e9e6e1 0%,#f5f5f5 40%,#d9d9d9 70%,#eeeeee 100%)}
.dots{height:5px;background-image:radial-gradient(circle,#e9a58a 0.8px,transparent 1px);background-size:3px 3px}
.band .dots{background-image:radial-gradient(circle,#f6b99e 0.8px,transparent 1px)}
.band-brand{left:0;width:814px;top:452px;display:flex;justify-content:center}
.band-brand .brand{font-size:12px;color:#2b2b2b}
.band-brand .dot{width:10px;height:10px;background:#2b2b2b}
.intro{left:68px;top:497px;width:678px;color:#fff;font-size:9.4px;line-height:13.6px;text-align:center}
.intro p+p{margin-top:13px}
.shadow{height:18px;border-radius:50%;background:radial-gradient(ellipse at center top,rgba(0,0,0,.22),transparent 70%)}
.section-title{left:140px;top:645px;font-family:"PT Sans",sans-serif;font-weight:700;font-size:16px;color:#222}
.grey-dots{background-image:radial-gradient(circle,#9a9a9a 0.7px,transparent 1px)}
.boxes-img{left:82px;top:680px;width:170px;height:150px;border-radius:6px;background:radial-gradient(ellipse at 45% 45%,#c49a6c 0%,#dcc3a4 35%,#f4f4f4 72%)}
.about{left:262px;top:678px;width:276px;font-size:8.4px;line-height:12.1px;text-align:justify;color:#222}
.about p+p{margin-top:12px}
.video{left:554px;top:658px;width:192px;height:136px;background:#2f2f2f;border-radius:3px;padding:5px}
.video .screen{width:182px;height:118px;background:linear-gradient(135deg,#e8eef2,#6d8aa3 55%,#233a63)}
.video .play{left:82px;top:46px;width:32px;height:32px;border-radius:50%;background:rgba(40,40,40,.75);border:2px solid #ddd}
.video .bar{left:8px;top:114px;width:176px;height:10px;font-size:5.5px;color:#ddd;display:flex;align-items:center;gap:4px}
.video .track{flex:1;height:2px;background:#777}
.divider{left:70px;top:830px;width:675px;border-top:1px dashed #bbb}
.card{width:210px;height:106px;top:862px;border-radius:5px;background:linear-gradient(#f0f0f0,#fafafa);box-shadow:0 2px 3px rgba(0,0,0,.06)}
.card h3{position:absolute;left:16px;top:7px;font-family:"PT Sans",sans-serif;font-size:13.5px;font-weight:700;color:#333}
.card .icon{position:absolute;left:16px;top:34px;width:60px;height:58px;border-radius:9px;background:linear-gradient(#fff,#d6d6d6);box-shadow:0 2px 3px rgba(0,0,0,.3);display:flex;align-items:center;justify-content:center}
.card p{position:absolute;left:91px;top:35px;width:112px;font-size:8.2px;line-height:12.2px;color:#555}
.footer{left:0;top:1010px;width:814px;height:166px;background:linear-gradient(#f3f3f3,#fafafa)}
.footer-line{left:70px;top:1010px;width:675px;border-top:2px dotted #c8c8c8}
.footer h4{position:absolute;font-family:"PT Sans",sans-serif;font-weight:400;font-size:15px;color:#333}
.vsep{position:absolute;top:1018px;width:1px;height:134px;background:#d5d5d5}
.social-item{position:absolute;left:84px;display:flex;align-items:center;gap:6px;font-family:"PT Sans",sans-serif;font-size:14px;font-weight:700;color:#2a5a9a}
.social-item .sq{width:18px;height:18px;background:#2a5a9a;border-radius:2px}
.links{position:absolute;list-style:none;font-size:8.2px;letter-spacing:.4px;color:#333}
.links li{height:16.3px;padding-left:8px;position:relative}
.links li::before{content:"";position:absolute;left:0;top:2px;border-left:3px solid #333;border-top:2.5px solid transparent;border-bottom:2.5px solid transparent}
.field{position:absolute;left:574px;width:143px;border:1px solid #cfcfcf;border-radius:9px;background:#fff;font-size:7.8px;color:#444;padding:8px 0 0 12px}
.submit{left:662px;top:1153px;width:53px;height:19px;border-radius:9px;background:linear-gradient(#3aa0ea,#126fc0);color:#fff;font-size:8.5px;font-weight:700;text-align:center;line-height:19px}
.copyright{left:0;top:1176px;width:814px;height:24px;background:var(--footer);color:#ddd;font-size:8.4px;text-align:center;line-height:24px}
</style>
</head>
<body>

<header class="abs header">
  <div class="abs brand"><span class="dot"></span>PARCEL BRISK</div>
  <div class="abs account">Sign Up &nbsp; / &nbsp; Login</div>
  <div class="abs follow-label">Follow Us on:</div>
  <div class="abs social-icons">
    <span style="background:#3b5b99"></span><span style="background:#4ab0e3"></span><span style="background:#1a77b5"></span><span style="background:#f07a24"></span><span style="background:#5d7fa8"></span><span style="background:#333"></span>
  </div>
</header>

<nav class="abs nav">
  <a class="home" href="#">HOME</a>
  <a href="#" style="left:185px;top:10px">ABOUT US</a>
  <span class="sep" style="left:235px"></span>
  <a href="#" style="left:282px;top:10px">CAREERS</a>
  <span class="sep" style="left:329px"></span>
  <a href="#" style="left:376px;top:10px">CONTACT</a>
  <span class="sep" style="left:424px"></span>
  <a href="#" style="left:478px;top:10px">LOCATIONS</a>
  <span class="sep" style="left:529px"></span>
  <a href="#" style="left:574px;top:10px">SERVICES</a>
  <span class="sep" style="left:624px"></span>
  <a href="#" style="left:688px;top:10px">TECHNOLOGY</a>
</nav>

<div class="abs band"></div>
<div class="abs hero-frame"></div>
<div class="abs hero-img" role="img" aria-label="Courier holding a parcel beside a jet plane, globe and delivery trucks over a world map"></div>

<div class="abs dots" style="left:142px;top:461px;width:228px;background-image:radial-gradient(circle,#f8c1a8 0.8px,transparent 1px)"></div>
<div class="abs dots" style="left:462px;top:461px;width:228px;background-image:radial-gradient(circle,#f8c1a8 0.8px,transparent 1px)"></div>
<div class="abs band-brand"><div class="brand"><span class="dot"></span>PARCEL BRISK</div></div>

<div class="abs intro">
  <p>Harlow Partners is a business advisory firm focuses on assisting businesses reach their potential. We understand and are passionate about small and medium sized businesses. Through the provision of sound long term advice we aim to build strong ongoing relationships with our clients.</p>
  <p>We offer business ongoing accounting services and advice, as well as provide consulting services to help businesses through difficult times. As a Chartered Accounting Firm with a strong technical accounting background and considerable experience in assisting business dealing with significant issues within their business. Harlow Partners can assist your business reach its full potential.</p>
</div>

<div class="abs shadow" style="left:80px;top:612px;width:290px"></div>
<div class="abs shadow" style="left:450px;top:612px;width:290px"></div>

<div class="abs grey-dots" style="left:72px;top:653px;width:62px;height:5px;background-size:3px 3px"></div>
<h2 class="abs section-title">What We Do</h2>
<div class="abs grey-dots" style="left:238px;top:653px;width:296px;height:5px;background-size:3px 3px"></div>

<div class="abs boxes-img" role="img" aria-label="Stack of cardboard boxes with a computer mouse"></div>
<div class="abs about">
  <p><b>Lorem ipsum dolor sit amet, consectetuer adipiscing elit. Nam cursus. Morbi ut mi. Nullam enim leo, egestas id,</b> condimentum at, laoreet mattis, massa. Sed eleifend nonummy diam. Praesent mauris ante, elementum et, bibendum at, posuere sit amet, nibh. Duis tincidunt lectus quis dui viverra vestibulum. Suspendisse vulputate aliquam dui. Nulla elementum dui ut augue. Aliquam vehicula mi at mauris. Maecenas placerat, nisl at consequat rhoncus, sem nunc gravida justo, quis eleifend arcu velit quis lacus.</p>
  <p>Pellentesque habitant morbi tristique senectus et netus et malesuada fames ac turpis egestas. In posuere felis nec tortor. Pellentesque faucibus. Ut accumsan ultricies elit...</p>
</div>

<div class="abs video">
  <div class="screen" role="img" aria-label="Video still of a smiling courier in a blue uniform"></div>
  <div class="abs play"><svg width="28" height="28" viewBox="0 0 28 28"><path d="M11 8 L20 14 L11 20 Z" fill="#eee"/></svg></div>
  <div class="abs bar"><span>■</span><span>❚❚</span><span class="track"></span><span>00:38/01:29</span></div>
</div>
<div class="abs shadow" style="left:560px;top:796px;width:180px;height:10px"></div>

<div class="abs divider"></div>

<div class="abs card" style="left:64px">
  <h3>EZY Quote</h3>
  <div class="icon"><svg width="40" height="26" viewBox="0 0 40 26"><circle cx="10" cy="16" r="9" fill="#1d4f8f"/><circle cx="29" cy="16" r="9" fill="#1d4f8f"/><path d="M3 14 Q5 3 15 1 L15 5 Q8 7 7 14Z M22 14 Q24 3 34 1 L34 5 Q27 7 26 14Z" fill="#1d4f8f"/></svg></div>
  <p>We focus on getting you the best return for your advertising dollar, while you focus on running your business.</p>
</div>
<div class="abs card" style="left:302px">
  <h3>EZY Send</h3>
  <div class="icon"><svg width="38" height="34" viewBox="0 0 38 34"><rect x="3" y="12" width="32" height="20" fill="#fff" stroke="#333" stroke-width="2.5"/><path d="M3 12 L19 24 L35 12 M3 32 L15 21 M35 32 L23 21" fill="none" stroke="#333" stroke-width="2.5"/><path d="M19 1 L26 8 L22 8 L22 15 L16 15 L16 8 L12 8Z" fill="#333"/></svg></div>
  <p>We focus on getting you the best return for your advertising dollar, while you focus on running your business.</p>
</div>
<div class="abs card" style="left:530px">
  <h3>EZY Trak</h3>
  <div class="icon" style="background:linear-gradient(#f6884e,#d94a16)"><svg width="34" height="34" viewBox="0 0 34 34"><circle cx="14" cy="14" r="10" fill="#6fb6ef" stroke="#333" stroke-width="3"/><path d="M21 21 L31 31" stroke="#333" stroke-width="5" stroke-linecap="round"/></svg></div>
  <p>We focus on getting you the best return for your advertising dollar, while you focus on running your business.</p>
</div>
<div class="abs shadow" style="left:80px;top:970px;width:180px;height:8px"></div>
<div class="abs shadow" style="left:318px;top:970px;width:180px;height:8px"></div>
<div class="abs shadow" style="left:546px;top:970px;width:180px;height:8px"></div>

<footer>
  <div class="abs footer"></div>
  <div class="abs footer-line"></div>
  <h4 style="left:83px;top:1018px">FOLLOW US</h4>
  <div class="social-item" style="top:1052px"><span class="sq"></span>Facenet</div>
  <div class="social-item" style="top:1093px"><span class="sq" style="background:#3aa5dd"></span>Chirper</div>
  <div class="social-item" style="top:1132px;color:#111"><span class="sq" style="background:#1a77b5"></span>WorkLink</div>
  <span class="vsep" style="left:202px"></span>
  <h4 style="left:218px;top:1024px">Company Information</h4>
  <ul class="links" style="left:220px;top:1052px">
    <li>About ShipCo</li><li>Careers</li><li>Conditions of Carriage</li><li>Open an Account</li><li>Register for a Login</li>
  </ul>
  <span class="vsep" style="left:373px"></span>
  <h4 style="left:407px;top:1024px">Customer Support</h4>
  <ul class="links" style="left:406px;top:1050px">
    <li>International Support</li><li>Domestic Support</li><li>ShipCo Services</li><li>International Services</li><li>Domestic Services</li>
  </ul>
  <span class="vsep" style="left:558px"></span>
  <h4 style="left:576px;top:1020px">Contact Now</h4>
  <div class="field" style="top:1048px;height:24px">----Name----</div>
  <div class="field" style="top:1077px;height:24px">----Email----</div>
  <div class="field" style="top:1106px;height:44px">---- Your Message ------</div>
  <div class="abs submit">Submit</div>
  <div class="abs copyright">Copyright © 2013 Parcel Brisk Courier, LLC. All rights reserved.</div>
</footer>

</body>
</html>
```